Help our Crumb Parlour find our winning design! We're looking for a business card....

We’re a Crumb Parlour in NY specializing in custom-made cakes and unique desserts.
Our cakes combine flavor and art, each designed to match customer’s special event and theme.
We’d like a unique business card with a clean design that will combine French chic and artistic look & feel.
We’d like to differentiate ourselves from standard bakeries, please don’t offer cupcake images :-)
Our logo is peach-pink and brown and we’d love to use these colors ( . Another color that can be added is gold - or feel free to suggest!

Target Market(s)

Women, ages 25-55

Industry/Entity Type

Boutique

Contact Information for Business Card

Text on card:
Logo
Crumb Parlour by Dana Whitfield

www.xxxxxxxx.com
xxx@xxxxx.com
(516) xxx-xxxx
F – xxxxxxxxxx
IG - xxxxxxxxx

Font styles to use
Sans Serif
Script

Requirements
Must have
• Logo
• Clean look
• French chic and artistic look & feel.
Nice to have
• Damask pattern
Should not have
• Cupcake images

```html
<!DOCTYPE html>
<html lang="en">
<head>
<meta charset="utf-8">
<title>Crumb Parlour by Dana Whitfield — Business Card</title>
<link rel="stylesheet" href="https://fonts.googleapis.com/css2?family=Exo+2:wght@500;600;800&family=Lobster&display=swap">
<style>
  :root {
    --cocoa: #8a4a22;
    --cocoa-deep: #7a3f1b;
    --cocoa-light: #9a5628;
    --caramel: #e0a25a;
    --caramel-soft: #d99a55;
    --script-fill: #c98a52;
    --script-edge: #a8683a;
    --peach-band: #dc9a52;
    --band-ink: #8a4a22;
    --sans: "Exo 2", "Helvetica Neue", Arial, sans-serif;
    --script: "Lobster", "Brush Script MT", cursive;
  }
  * { margin: 0; padding: 0; box-sizing: border-box; }
  html, body { width: 1200px; height: 747px; overflow: hidden; background: var(--cocoa); }
  .card {
    position: relative; width: 1200px; height: 747px; overflow: hidden;
    background: var(--cocoa);
  }
  .cake-photo {
    position: absolute; inset: 0;
    background: radial-gradient(ellipse 55% 70% at 50% 45%, var(--cocoa-light) 0%, var(--cocoa) 60%, var(--cocoa-deep) 100%);
  }
  .rule {
    position: absolute; height: 0;
    border-top: 2px dotted var(--caramel-soft);
    opacity: .85;
  }
  .rule--left { left: 0; width: 387px; top: 139px; }
  .rule--right { left: 775px; width: 425px; top: 139px; }
  .rule--upper { left: 294px; width: 554px; top: 380px; }
  .rule--lower { left: 294px; width: 554px; top: 458px; }
  .center { position: absolute; left: 0; width: 100%; text-align: center; }
  .brand-title {
    top: 110px; font-family: var(--sans); font-weight: 800; font-size: 40px;
    letter-spacing: 1px; color: var(--caramel);
    text-shadow: 0 3px 6px rgba(60,25,5,.45);
  }
  .brand-by, .brand-owner {
    font-family: var(--script); color: var(--script-fill);
    -webkit-text-stroke: 1.5px var(--script-edge);
    text-shadow: 0 4px 6px rgba(60,25,5,.5);
  }
  .brand-by { top: 170px; font-size: 66px; }
  .brand-owner { top: 268px; font-size: 70px; }
  .contact {
    top: 386px; font-family: var(--sans); font-weight: 600; font-size: 26px;
    line-height: 29px; color: var(--caramel);
  }
  .phone {
    position: absolute; top: 472px; left: 463px; width: 200px; text-align: center;
    font-family: var(--sans); font-weight: 600; font-size: 27px; color: var(--caramel);
  }
  .social-band {
    position: absolute; left: 0; top: 521px; width: 1200px; height: 169px;
    background: var(--peach-band);
    box-shadow: 0 -3px 8px rgba(60,25,5,.35), 0 5px 10px rgba(60,25,5,.5);
  }
  .social-row {
    position: absolute; left: 404px; display: flex; align-items: center; gap: 24px;
    font-family: var(--sans); font-weight: 600; font-size: 28px; color: var(--band-ink);
  }
  .social-row--first { top: 566px; }
  .social-row--second { top: 607px; }
  .social-mark { width: 32px; height: 32px; border-radius: 5px; background: var(--band-ink); flex: none; }
</style>
</head>
<body>
  <main class="card">
    <div class="cake-photo" role="img" aria-label="Faint photograph of a decorated custom cake with chocolate curls"></div>

    <div class="rule rule--left"></div>
    <div class="rule rule--right"></div>
    <h1 class="center brand-title">CRUMB PARLOUR</h1>
    <p class="center brand-by">By</p>
    <p class="center brand-owner">Dana Whitfield</p>

    <div class="rule rule--upper"></div>
    <p class="center contact">www.CrumbParlourNY.com<br>dana@CrumbParlourNY.com</p>
    <div class="rule rule--lower"></div>
    <p class="phone">(516) 482-1937</p>

    <section class="social-band"></section>
    <div class="social-row social-row--first"><span class="social-mark"></span>CrumbParlourCakes</div>
    <div class="social-row social-row--second"><span class="social-mark"></span>CrumbParlourCakes</div>
  </main>
</body>
</html>
```